New business card for my lawn and landscape business

Dorrin Yard and Building is a full-service lawn care, landscaping, and light construction company serving Paragould and the Northeast Arkansas region. The business is owned and operated by Marcus Toller, with a reputation for hands-on, detail-oriented service, dependable crews, and quality results for both residential and commercial clients. A well regarded business with great reviews.
Owner Marcus Toller
Dorrinyardandbuilding.example

Target Market(s)

Commercial, Middle, and upper class in north east Arkansas

Industry/Entity Type

Lawn maintenance and landscape

Contact Information for Business Card

Dorrin Yard And Building Professional lawn care, landscaping, and property improvement in Northeast Arkansas. • lawn maintenance •lawn treatments and weed control • exterior projects • Custom landscape design & installation • Sod, trees, rock & drainage solutions • Residential & commercial services Reliable. Detailed. Done right.

Requirements
Must have
• Business name, service area, list of some of our services, clean design that represents
Nice to have
• Unique. Different design element than just grass because its already in n the logo. Picture of a warm season (south) lawn or landscape. Pictures of the type of work we do

```html
<!DOCTYPE html>
<html lang="en">
<head>
<meta charset="utf-8">
<title>Dorrin Yard and Building – Business Card</title>
<link rel="stylesheet" href="https://fonts.googleapis.com/css2?family=Poppins:wght@400;600;700&display=swap">
<style>
  :root {
    --green: #6cae3e;
    --green-deep: #2f7a1c;
    --green-light: #8fd14f;
    --ink: #555a5e;
    --rule: #6b6b6b;
    --paper: #ffffff;
    --backdrop: #e4e4e2;
  }
  * { box-sizing: border-box; margin: 0; padding: 0; }
  html, body {
    width: 1200px; height: 801px; overflow: hidden;
    background: var(--backdrop);
    font-family: "Poppins", sans-serif;
  }
  .sheet {
    width: 1200px; height: 801px;
    display: flex; align-items: center; justify-content: center; gap: 40px;
  }
  .card {
    width: 550px; height: 314px;
    background: var(--paper);
    position: relative; overflow: hidden;
    box-shadow: 0 6px 18px rgba(0,0,0,.15);
  }

  /* Front */
  .front-logo {
    position: absolute; top: 52px; left: 0; right: 0;
    display: flex; align-items: center; justify-content: center; gap: 12px;
  }
  .front-logo .mark-dot {
    width: 22px; height: 22px; border-radius: 50%; background: var(--green);
  }
  .front-logo .wordmark {
    font-weight: 700; font-size: 26px; color: var(--green); letter-spacing: .5px;
  }
  .front-details {
    position: absolute; top: 150px; left: 0; right: 0;
    display: flex; justify-content: center; align-items: center; gap: 22px;
  }
  .person { text-align: right; }
  .person-name { font-weight: 700; font-size: 26px; color: var(--green); line-height: 1.1; }
  .person-role { font-size: 15px; color: var(--ink); }
  .divider { width: 1px; height: 80px; background: var(--rule); }
  .contact { list-style: none; font-size: 14px; color: var(--ink); line-height: 1.6; }
  .contact li { display: flex; align-items: center; gap: 7px; }
  .contact svg { width: 12px; height: 12px; fill: var(--green); flex: none; }
  .contact .no-icon { padding-left: 19px; }

  /* Back */
  .back-photo {
    position: absolute; top: 0; left: 0; right: 0; height: 160px;
    background: linear-gradient(160deg, var(--green-light) 0%, #4f9a28 45%, var(--green-deep) 100%);
  }
  .back-logo {
    position: absolute; top: 55px; left: 0; right: 0;
    display: flex; align-items: center; justify-content: center; gap: 10px;
  }
  .back-logo .mark-dot { width: 18px; height: 18px; border-radius: 50%; background: var(--paper); }
  .back-logo .wordmark { font-weight: 700; font-size: 22px; color: var(--paper); }
  .back-text {
    position: absolute; top: 170px; left: 20px; right: 20px; text-align: center;
  }
  .tagline { font-weight: 700; font-size: 14px; color: var(--green); line-height: 1.3; margin-bottom: 7px; }
  .services { font-size: 12.5px; color: var(--ink); line-height: 1.45; }
  .services .bullet { color: var(--green); }
</style>
</head>
<body>
<main class="sheet">
  <section class="card card-front">
    <div class="front-logo">
      <span class="mark-dot"></span>
      <span class="wordmark">Dorrin Yard and Building</span>
    </div>
    <div class="front-details">
      <div class="person">
        <div class="person-name">Marcus Toller</div>
        <div class="person-role">Owner</div>
      </div>
      <div class="divider"></div>
      <ul class="contact">
        <li><svg viewBox="0 0 24 24"><path d="M6.6 10.8a15.1 15.1 0 0 0 6.6 6.6l2.2-2.2c.3-.3.7-.4 1-.2 1.1.4 2.3.6 3.6.6.6 0 1 .4 1 1V20c0 .6-.4 1-1 1A17 17 0 0 1 3 4c0-.6.4-1 1-1h3.5c.6 0 1 .4 1 1 0 1.3.2 2.5.6 3.6.1.3 0 .7-.2 1z"/></svg>(870) 555-0148</li>
        <li><svg viewBox="0 0 24 24"><circle cx="12" cy="12" r="11"/></svg>Dorrinyardandbuilding.example</li>
        <li class="no-icon">Greyford, AR 72999</li>
      </ul>
    </div>
  </section>

  <section class="card card-back">
    <div class="back-photo" role="img" aria-label="Close-up photograph of fresh green grass blades"></div>
    <div class="back-logo">
      <span class="mark-dot"></span>
      <span class="wordmark">Dorrin Yard and Building</span>
    </div>
    <div class="back-text">
      <p class="tagline">Dorrin Yard And Building Professional lawn care<br>landscaping, and property improvement in Northeast Arkansas</p>
      <p class="services">
        <span class="bullet">●</span> lawn maintenance <span class="bullet">●</span> lawn treatments and weed control<br>
        <span class="bullet">●</span> exterior projects <span class="bullet">●</span> Custom landscape design &amp; installation<br>
        <span class="bullet">●</span> Sod, trees, rock &amp; drainage solutions<br>
        <span class="bullet">●</span> Residential &amp; commercial services Reliable. Detailed. Done right
      </p>
    </div>
  </section>
</main>
</body>
</html>
```